Lirra - food stand (booth) design

We need posters for a small food stand situated in the centre of the city directly in front of a high-class shopping mall (see file 2 - the food stand at the square) . We sell cinnamon rolls which we named Lirra. We are looking for a design of the food stand which would lure the customer from the square in front of the mall of a size 30 meters (100 ft) wide. At the same time, it should be elegant, possibly Provence style in pastel colours.

We need the name and description of the product (meaning: Lirra – cinnamon rolls) to be visible from the front and maybe even the sides of the food stand. At the same time, we need to place the menu on some "wings", attached to the sides of the stand from outside. The menu will consist of 8 products (4 different kinds of Lirra rolls and 4 kinds of coffee). If you could visualize the wings, it would be nice.

We also need the design of the packaging of the product (a box similar to a hamburger box and a coffee cup) which might carry the logo (which we do not have), but again that is up to you. If you design the logo, maybe it should be placed on the outside of the food stand (up to you).

See the enclosed photos of the food stand from the front and the sides. The size of the food stand’s plan view is 2.5 x 2 meters (8.2 x 6.56 ft). The design can be either in the size of the current stickers (which would be replaced by yours) or it can cover the whole stand.

Below are sizes of the panels. We notice only the relevant ones
(for example the upper front is irrelevant, because it's always open, thus invisible). First is always x (eg. horizontal) axis. All sizes in centimeters.
A Front
A1 lower 234 x 40 cm
B Left side
B1 upper 174 x 100 cm
B2 lower 184 x 48 cm
C Right side (with the door)
C1 left 100 x 100 cm
C2 right (door) 48 x 184 cm

We are looking forward to your designs!

Thank you,
Team Lirra

```html
<!DOCTYPE html>
<html lang="en">
<head>
<meta charset="utf-8">
<title>Lirra – Bakery and Coffee stand panels</title>
<link rel="stylesheet" href="https://fonts.googleapis.com/css2?family=Cinzel:wght@700&display=swap">
<style>
  :root {
    --stage: #ecebe6;
    --cream: #f9e8c4;
    --cream-deep: #f1d7a6;
    --stripe-light: #f8e4b9;
    --stripe-dark: #efd19b;
    --brown: #5a1c11;
    --roll-light: #e9b878;
    --roll-dark: #9c5a2a;
    --coffee-light: #b6733a;
    --coffee-dark: #3d1a0b;
  }
  * { margin: 0; padding: 0; box-sizing: border-box; }
  html, body {
    width: 1200px;
    height: 1114px;
    overflow: hidden;
    background: var(--stage);
  }
  .stand-panels {
    position: relative;
    width: 1200px;
    height: 1114px;
  }
  .panel {
    position: absolute;
    left: 40px;
    width: 1120px;
    box-shadow: 0 2px 8px rgba(0,0,0,0.15);
  }
  .panel--upper { top: 170px; height: 505px; }
  .panel--lower { top: 715px; height: 220px; }
  .panel svg { display: block; width: 100%; height: 100%; }
  .headline, .label, .brand-name, .brand-tagline {
    font-family: "Cinzel", serif;
    font-weight: 700;
    fill: var(--brown);
  }
  .headline { font-size: 74px; letter-spacing: 1px; }
  .label { font-size: 58px; }
  .brand-name, .brand-tagline { text-anchor: middle; }
  .brand-tagline { letter-spacing: 2px; }
</style>
</head>
<body>
<main class="stand-panels">

  <section class="panel panel--upper" aria-label="Upper side panel">
    <svg viewBox="0 0 1120 505" xmlns="http://www.w3.org/2000/svg">
      <defs>
        <radialGradient id="upper-ground" cx="50%" cy="50%" r="70%">
          <stop offset="0" stop-color="var(--cream)"/>
          <stop offset="1" stop-color="var(--cream-deep)"/>
        </radialGradient>
        <path id="headline-arc" d="M140 225 Q567 -5 990 240"/>
      </defs>
      <rect class="swirl-ground" role="img" aria-label="Soft cream swirl pattern background"
            width="1120" height="505" fill="url(#upper-ground)"/>
      <text class="headline">
        <textPath href="#headline-arc" startOffset="50%" text-anchor="middle">BAKERY AND COFFEE</textPath>
      </text>
      <text class="brand-name" x="560" y="345" font-size="150">Lirra</text>
      <text class="brand-tagline" x="560" y="420" font-size="40">CINNAMON ROLLS</text>
    </svg>
  </section>

  <section class="panel panel--lower" aria-label="Lower front panel">
    <svg viewBox="0 0 1120 220" xmlns="http://www.w3.org/2000/svg">
      <defs>
        <linearGradient id="lower-ground" x1="0" y1="0" x2="1" y2="0">
          <stop offset="0" stop-color="var(--stripe-light)"/>
          <stop offset="0.5" stop-color="var(--stripe-dark)"/>
          <stop offset="1" stop-color="var(--stripe-light)"/>
        </linearGradient>
        <radialGradient id="rolls-photo" cx="40%" cy="50%" r="65%">
          <stop offset="0" stop-color="var(--roll-light)"/>
          <stop offset="1" stop-color="var(--roll-dark)"/>
        </radialGradient>
        <linearGradient id="coffee-photo" x1="0" y1="1" x2="1" y2="0">
          <stop offset="0" stop-color="var(--coffee-light)" stop-opacity="0.6"/>
          <stop offset="1" stop-color="var(--coffee-dark)"/>
        </linearGradient>
        <path id="bakery-arc" d="M134 70 Q330 90 440 210"/>
        <path id="coffee-arc" d="M742 205 Q850 85 1025 70"/>
      </defs>
      <rect class="stripe-ground" role="img" aria-label="Cream vertical stripe pattern background"
            width="1120" height="220" fill="url(#lower-ground)"/>
      <rect class="rolls-photo" role="img" aria-label="Photo of iced cinnamon rolls"
            x="0" y="0" width="265" height="220" fill="url(#rolls-photo)" opacity="0.85"/>
      <rect class="coffee-photo" role="img" aria-label="Photo of coffee splashing from a cup"
            x="790" y="35" width="330" height="180" fill="url(#coffee-photo)" opacity="0.8"/>
      <text class="label">
        <textPath href="#bakery-arc" startOffset="50%" text-anchor="middle">BAKERY</textPath>
      </text>
      <text class="brand-name" x="569" y="118" font-size="66">Lirra</text>
      <text class="brand-tagline" x="569" y="150" font-size="18">CINNAMON ROLLS</text>
      <text class="label">
        <textPath href="#coffee-arc" startOffset="50%" text-anchor="middle">COFFEE</textPath>
      </text>
    </svg>
  </section>

</main>
</body>
</html>
```